Law Firm Business Card

This is a business card for a law firm that serves US military and veterans.

The card must have ONLY the following (we want an uncluttered look):

- Company logo (PNG, GIF, JPEG copies uploaded)
- A tagline reading: "a law firm for service members and veterans"
- My name and title: "Martin Okello" and "Attorney"
- My email: "martin.okello@harborlinecounsel.com"
- My number: "855-FILE-NOW (345-3669)"

We are looking for a clean, simple layout with only the above information, likely printed on a bright white cotton stock. The font of our logo is DIN 1451, and the font used on our website is Helvetica Neue. The color of our logo is #336699, and we probably want the tagline in that color also, and my contact information in a dark grey. Please review our website at www.harborlinecounsel.com to ensure your card design complements our website style.

Thanks and we look forward to seeing your submissions.

A few notes:

- Two-sided submissions are ok
- Please don't add graphics (scales of justice, judges hammer, etc)

```html
<!DOCTYPE html>
<html lang="en">
<head>
<meta charset="utf-8">
<title>Harborline Counsel — Business Card</title>
<link rel="stylesheet" href="https://fonts.googleapis.com/css2?family=Barlow:wght@400;500&family=Inter:wght@300;400&display=swap">
<style>
  :root {
    --backdrop: #b4b4b4;
    --stock: #fbfbfa;
    --brand-blue: #336699;
    --ink-grey: #555555;
    --ink-soft: #6a6a6a;
  }
  * { box-sizing: border-box; margin: 0; padding: 0; }
  html, body {
    width: 1200px; height: 720px; overflow: hidden;
    background: var(--backdrop);
  }
  .sheet {
    width: 1200px; height: 720px;
    display: flex; align-items: center; justify-content: center; gap: 48px;
  }
  .card {
    width: 525px; height: 300px;
    background: var(--stock);
    box-shadow: 0 2px 6px rgba(0,0,0,0.18);
    position: relative;
  }

  /* Front face */
  .card-front { display: flex; flex-direction: column; align-items: center; }
  .firm-name {
    margin-top: 100px;
    font-family: "Barlow", "Helvetica Neue", sans-serif;
    font-weight: 500;
    font-size: 40px;
    line-height: 1.1;
    color: var(--brand-blue);
    text-align: center;
  }
  .tagline {
    position: absolute; bottom: 26px; left: 0; right: 0;
    text-align: center;
    font-family: "Barlow", "Helvetica Neue", sans-serif;
    font-weight: 400;
    font-size: 15px; letter-spacing: 0.4px;
    color: var(--brand-blue);
    text-transform: uppercase;
  }

  /* Back face */
  .card-back {
    display: flex; flex-direction: column; align-items: center;
    padding-top: 52px;
    font-family: "Inter", "Helvetica Neue", sans-serif;
  }
  .person-name {
    font-weight: 300; font-size: 25px; color: var(--ink-grey);
    text-transform: uppercase; letter-spacing: 0.2px;
  }
  .person-title {
    font-weight: 300; font-size: 14px; color: var(--ink-soft);
    margin-top: 2px; margin-left: 40px;
  }
  .divider-star { width: 12px; height: 12px; margin: 20px 0 12px; }
  .divider-star path { fill: var(--brand-blue); }
  .contact-label {
    font-weight: 400; font-size: 14px; color: var(--brand-blue);
    text-transform: uppercase; letter-spacing: 0.3px;
  }
  .contact-value {
    font-weight: 300; font-size: 15px; color: var(--ink-grey);
    margin-top: 2px; margin-bottom: 12px;
  }
</style>
</head>
<body>
  <main class="sheet">
    <section class="card card-front" aria-label="Card front">
      <h1 class="firm-name">Harborline Counsel</h1>
      <p class="tagline">A law firm for service members and veterans</p>
    </section>

    <section class="card card-back" aria-label="Card back">
      <h2 class="person-name">Martin Okello</h2>
      <p class="person-title">Attorney</p>
      <svg class="divider-star" viewBox="0 0 24 24" aria-hidden="true">
        <path d="M12 1.5l3.1 7.2 7.8.6-5.9 5.1 1.8 7.6L12 18l-6.8 4 1.8-7.6-5.9-5.1 7.8-.6z"/>
      </svg>
      <p class="contact-label">Phone</p>
      <p class="contact-value">855-FILE-NOW (345-3669)</p>
      <p class="contact-label">Email</p>
      <p class="contact-value">martin.okello@harborlinecounsel.com</p>
    </section>
  </main>
</body>
</html>
```